I need a website for my moving company Bolt Hauling LLC. I would like the following text included in my website. I have purchased the domain bolthaulingcrew.example from siteburrow.example. I am not familiar with SEO or other techniques that help my page on search engines but would like the website to be optimized for Findora search engine. I have attached our logo below and would like it to be used in the design. The colors in the logo can be used also in the design.
Home/About Us
At Bolt Hauling LLC, we know moving. It can be difficult, stressful, and a real pain in the backside. But it doesn’t have to be! When you partner with Bolt, you get the benefits of a professional moving team that is licensed and insured for your protection along with years of experience and a dedication to providing the highest quality service, each and every time.
Our Services
We do a wide variety of local moves, including apartments, single-family homes, retirement communities, dorms, condos, and many more! Our movers are trained to protect your belongings and your home – all pieces of furniture are padded and stretch wrapped free of charge, ensuring your items and home are damage-free at the end of your move. Having added stress about packing up your home prior to moving? We’ve got you covered with our full service packing and unpacking services, too.
What You Get
When you partner with BOLT, you’ll get the best service in the industry, as well as:
* The Use of Packing & Moving Materials: The hourly rate includes the use of our dollies, ratchet straps, pads, moving tools, and property protection like floor mats, door-jamb protectors, stairwell protectors, and plenty of muscle!
• Trained, Licensed, and Insured Movers: All of our movers are highly trained to provide you with the best service, and to ensure the protection of you and your items.
• Professional: Honest, Uniformed, Nice, Knowledgeable Service is what you’ll get with every member of our moving teams.
• Custom Service for Every Move: Every move is as unique as the person or business moving. Our training and equipment allows us to customize every project to ensure the very best for every client.
Target Market(s)
Home and Business movers
Industry/Entity Type
Moving Company
Colors
Designer to choose colors to be used in the design.
Requirements
Must have
- 2 sides
Nice to have
- Colorful design with logo included.
Should not have
- animated characters

```html
<!DOCTYPE html>
<html lang="en">
<head>
<meta charset="utf-8">
<title>Bolt Hauling LLC – We Know Moving</title>
<link href="https://fonts.googleapis.com/css2?family=Poppins:wght@400;500;600;700&family=Open+Sans:wght@400;600&family=Oswald:wght@400;500&family=Crimson+Text:ital@1&display=swap" rel="stylesheet">
<style>
:root{
  --orange:#f7941d;
  --orange-dark:#e8830f;
  --green:#7dc242;
  --green-dark:#5e9a2c;
  --ink:#2b2b2b;
  --text:#555;
  --muted:#888;
  --light:#f2f2f2;
  --line:#e3e3e3;
  --footer:#1d1d1d;
  --footer-deep:#151515;
  --white:#fff;
}
*{box-sizing:border-box;margin:0;padding:0}
html,body{width:1200px;height:2311px;overflow:hidden}
body{font-family:"Open Sans",sans-serif;color:var(--text);background:var(--white)}
.page{position:relative;width:1200px;height:2311px;overflow:hidden}
.abs{position:absolute}

/* header */
.top-rule{left:0;top:0;width:1200px;height:6px;background:linear-gradient(90deg,var(--orange),var(--green))}
.brand{left:80px;top:52px;display:flex;align-items:center;gap:10px}
.brand-mark{width:22px;height:22px;background:var(--orange)}
.brand-name{font-family:"Poppins",sans-serif;font-weight:700;font-size:20px;color:var(--orange);letter-spacing:.2px}
.contact-item{top:34px;display:flex;gap:12px;align-items:flex-start}
.contact-item svg{flex:none;margin-top:4px}
.contact-label{font-family:"Poppins",sans-serif;font-weight:600;font-size:12px;color:var(--ink)}
.contact-value{font-size:11px;color:var(--text);line-height:1.35;margin-top:2px}
.book-btn{left:969px;top:34px;width:152px;height:42px;background:var(--orange);border-bottom:3px solid var(--orange-dark);color:#fff;font-family:"Poppins",sans-serif;font-weight:500;font-size:13px;display:flex;align-items:center;justify-content:center;gap:8px}
.nav-bar{left:565px;top:102px;width:635px;height:40px;background:var(--green);clip-path:polygon(40px 0,100% 0,100% 100%,0 100%)}
.nav{left:615px;top:102px;height:40px;display:flex;align-items:center;gap:30px;font-family:"Poppins",sans-serif;font-weight:500;font-size:12.5px;color:#fff}

/* hero */
.hero{left:0;top:142px;width:1200px;height:496px;background:linear-gradient(90deg,#8a6a4c 0%,#a98a63 30%,#8fb85a 60%,var(--green) 80%,#88c648 100%)}
.hero-shade{left:0;top:142px;width:1200px;height:496px;background:linear-gradient(90deg,rgba(0,0,0,.35),rgba(0,0,0,0) 55%)}
.hero-title{left:80px;font-family:"Poppins",sans-serif;font-weight:600;font-size:44px;color:#fff;padding:0 22px;height:52px;line-height:54px;letter-spacing:.3px}
.t1{top:261px;background:var(--orange)}
.t2{top:316px;background:var(--green)}
.hero-copy{left:80px;top:384px;width:590px;font-size:14px;line-height:22px;color:#fff}
.hero-btn{left:80px;top:493px;width:165px;height:46px;border:2px solid #fff;color:#fff;font-family:"Poppins",sans-serif;font-weight:500;font-size:13px;display:flex;align-items:center;justify-content:center}
.hero-arrow{top:575px;width:44px;height:43px;background:#fff;display:flex;align-items:center;justify-content:center}

/* quote form */
.quote{left:765px;top:190px;width:355px;height:403px;background:var(--green-dark)}
.quote-head{position:absolute;left:0;top:0;width:355px;height:89px;background:var(--orange);display:flex;align-items:center;padding-left:26px;gap:16px}
.quote-title{font-family:"Oswald",sans-serif;font-weight:500;font-size:21px;color:#fff;letter-spacing:.3px}
.quote-sub{font-size:10px;color:#fff;margin-top:2px}
.field{position:absolute;left:27px;width:302px;height:42px;background:#fff;display:flex;align-items:center;justify-content:space-between;padding:0 14px;font-size:12px;color:var(--text)}
.quote-btn{position:absolute;left:27px;top:329px;width:302px;height:51px;background:var(--orange);color:#fff;font-family:"Poppins",sans-serif;font-weight:600;font-size:16px;display:flex;align-items:center;justify-content:center}

/* services */
.services{left:0;top:638px;width:1200px;height:653px;background:var(--light)}
.eyebrow{font-family:"Poppins",sans-serif;font-weight:600;font-size:11px;color:var(--orange);letter-spacing:.3px}
.section-title{font-family:"Poppins",sans-serif;font-weight:600;font-size:27px;color:var(--ink);letter-spacing:.8px}
.rule{width:36px;height:2px;background:var(--orange)}
.center{left:0;width:1200px;text-align:center}
.services-intro{left:260px;top:812px;width:680px;text-align:center;font-size:13px;line-height:22px;color:var(--ink)}
.service{width:360px;display:flex;gap:22px}
.diamond{flex:none;width:66px;height:66px;position:relative;margin-top:2px}
.service-name{font-family:"Poppins",sans-serif;font-weight:500;font-size:13px;color:var(--green);letter-spacing:.6px;margin-bottom:6px}
.service-copy{font-size:12px;line-height:21px;color:var(--muted)}
.mover-photo{left:460px;top:890px;width:296px;height:401px;background:radial-gradient(ellipse at 50% 40%,#6a7080 0%,#545a68 45%,rgba(242,242,242,0) 72%)}

/* testimonials & guarantee */
.card{top:1471px;height:248px;border:1px solid var(--line);background:#fff}
.quote-text{font-family:"Crimson Text",serif;font-style:italic;font-size:18px;line-height:25px;color:#444}
.quote-mark{left:112px;top:1490px;font-family:"Poppins",sans-serif;font-weight:700;font-size:110px;color:#f0f0f0;line-height:1}
.cite-name{font-family:"Poppins",sans-serif;font-weight:600;font-size:13px;color:var(--ink)}
.cite-role{font-size:13px;color:var(--muted)}
.dots{left:497px;top:1671px;display:flex;gap:5px}
.dots span{width:11px;height:11px;border-radius:50%;background:#e1e1e1}
.dots span:first-child{background:var(--green)}
.guarantee-lead{font-size:14px;line-height:22px;color:var(--ink)}
.perk{display:flex;align-items:center;gap:12px;font-size:12px;color:var(--text);margin-top:19px}

/* newsletter */
.newsletter{left:0;top:1779px;width:1200px;height:131px;background:var(--green)}
.newsletter-title{left:200px;top:1832px;font-family:"Poppins",sans-serif;font-weight:600;font-size:22px;color:#fff;letter-spacing:.4px}
.signup{left:555px;top:1823px;width:446px;height:46px;background:#fff;border-radius:23px;border:2px solid var(--orange);overflow:hidden;display:flex;align-items:center}
.signup-field{flex:1;padding-left:18px;font-size:12px;color:var(--text)}
.signup-btn{width:100px;height:100%;background:var(--orange);color:#fff;font-family:"Poppins",sans-serif;font-weight:600;font-size:13px;display:flex;align-items:center;justify-content:center}

/* footer */
.footer{left:0;top:1910px;width:1200px;height:401px;background:var(--footer)}
.footer-notch{left:1130px;top:1884px;width:70px;height:30px;background:var(--footer);clip-path:polygon(30px 0,100% 0,100% 100%,0 100%)}
.footer-base{left:0;top:2256px;width:1200px;height:55px;background:var(--footer-deep)}
.f-head{top:1976px;font-family:"Poppins",sans-serif;font-weight:600;font-size:13px;color:#fff}
.f-about{left:80px;top:2026px;width:400px;font-size:11.5px;line-height:21.5px;color:#bbb}
.f-list{top:2027px;font-size:11.5px;line-height:26.8px;color:#aaa;list-style:none}
.socials{left:80px;top:2157px;display:flex;gap:9px}
.socials span{width:27px;height:27px;background:#2a2a2a}
.f-contact{left:855px;top:2027px;font-size:11.5px;color:#aaa}
.f-contact div{display:flex;align-items:center;gap:10px;height:33px}
.copyright{left:0;top:2276px;width:1200px;text-align:center;font-size:11px;color:#555}
.to-top{left:1140px;top:2239px;width:40px;height:40px;background:var(--orange);border-radius:3px;display:flex;align-items:center;justify-content:center}
</style>
</head>
<body>
<div class="page">

  <!-- header -->
  <div class="abs top-rule"></div>
  <div class="abs brand"><span class="brand-mark"></span><span class="brand-name">BOLT HAULING</span></div>

  <div class="abs contact-item" style="left:305px">
    <svg width="22" height="22" viewBox="0 0 24 24"><path fill="#7dc242" d="M6.6 10.8a15.1 15.1 0 0 0 6.6 6.6l2.2-2.2c.3-.3.7-.4 1-.2 1.1.4 2.3.6 3.6.6.6 0 1 .4 1 1V20c0 .6-.4 1-1 1C10.6 21 3 13.4 3 4c0-.6.4-1 1-1h3.5c.6 0 1 .4 1 1 0 1.3.2 2.5.6 3.6.1.3 0 .7-.2 1z"/></svg>
    <div><div class="contact-label">ANY QUESTION AT</div><div class="contact-value">(555) 014-2290</div></div>
  </div>
  <div class="abs contact-item" style="left:497px">
    <svg width="20" height="26" viewBox="0 0 20 26"><path fill="#7dc242" d="M10 0a9 9 0 0 0-9 9c0 7 9 17 9 17s9-10 9-17a9 9 0 0 0-9-9zm0 12.5A3.5 3.5 0 1 1 10 5.5a3.5 3.5 0 0 1 0 7z"/></svg>
    <div><div class="contact-label">ADDRESS</div><div class="contact-value">42 Linden Row, Maplecrest,<br>ST 00412, US</div></div>
  </div>
  <div class="abs contact-item" style="left:708px">
    <svg width="26" height="18" viewBox="0 0 26 18"><rect width="26" height="18" rx="1" fill="#7dc242"/><path d="M1 1l12 9 12-9" stroke="#fff" stroke-width="2" fill="none"/></svg>
    <div><div class="contact-label">EMAIL US</div><div class="contact-value">info@bolthaulingcrew.example</div></div>
  </div>
  <div class="abs book-btn">
    <svg width="16" height="16" viewBox="0 0 16 16"><rect x="1" y="2.5" width="14" height="12" rx="1" fill="none" stroke="#fff" stroke-width="1.6"/><path d="M1 6.5h14M4.5 1v3M11.5 1v3" stroke="#fff" stroke-width="1.6"/></svg>
    BOOK TODAY
  </div>

  <div class="abs nav-bar"></div>
  <nav class="abs nav"><span>HOME</span><span>ABOUT US</span><span>SERVICES</span><span>PROJECTS</span><span>BLOG</span><span>CONTACT US</span></nav>

  <!-- hero -->
  <div class="abs hero" role="img" aria-label="Photo of a smiling couple carrying moving boxes into their new home"></div>
  <div class="abs hero-shade"></div>
  <h1 class="abs hero-title t1">BOLT HAULING LLC</h1>
  <div class="abs hero-title t2">WE KNOW MOVING</div>
  <p class="abs hero-copy">It can be difficult, stressful, and a real pain in the backside. But it doesn't have to be! When you partner with Bolt, you get the benefits of a professional moving team that is licensed and insured for your protection along with years of experience and a dedication to providing the highest quality service, each and every time.</p>
  <div class="abs hero-btn">BOOKING NOW</div>
  <div class="abs hero-arrow" style="left:80px"><svg width="10" height="14" viewBox="0 0 10 14"><path d="M8 1L2 7l6 6" stroke="#222" stroke-width="2" fill="none"/></svg></div>
  <div class="abs hero-arrow" style="left:128px"><svg width="10" height="14" viewBox="0 0 10 14"><path d="M2 1l6 6-6 6" stroke="#222" stroke-width="2" fill="none"/></svg></div>

  <form class="abs quote">
    <div class="quote-head">
      <svg width="44" height="40" viewBox="0 0 44 40"><path d="M22 3C11 3 3 10 3 18.5c0 4.6 2.4 8.7 6.2 11.5L7 37l8.6-4.2c2 .6 4.2.9 6.4.9 11 0 19-7 19-15.2S33 3 22 3z" fill="none" stroke="#fff" stroke-width="2.6"/><circle cx="14" cy="18.5" r="2.3" fill="#fff"/><circle cx="22" cy="18.5" r="2.3" fill="#fff"/><circle cx="30" cy="18.5" r="2.3" fill="#fff"/></svg>
      <div><div class="quote-title">GET AN INSTANT QUOTE</div><div class="quote-sub">It's free &amp; easy – no obligations</div></div>
    </div>
    <div class="field" style="top:113px"><span>Moving From</span><svg width="11" height="14" viewBox="0 0 20 26"><path fill="none" stroke="#444" stroke-width="2.4" d="M10 2a7.5 7.5 0 0 0-7.5 7.5C2.5 15 10 24 10 24s7.5-9 7.5-14.5A7.5 7.5 0 0 0 10 2z"/><circle cx="10" cy="9.5" r="2.6" fill="#444"/></svg></div>
    <div class="field" style="top:167px"><span>Moving To</span><svg width="11" height="14" viewBox="0 0 20 26"><path fill="none" stroke="#444" stroke-width="2.4" d="M10 2a7.5 7.5 0 0 0-7.5 7.5C2.5 15 10 24 10 24s7.5-9 7.5-14.5A7.5 7.5 0 0 0 10 2z"/><circle cx="10" cy="9.5" r="2.6" fill="#444"/></svg></div>
    <div class="field" style="top:221px"><span>When</span><svg width="13" height="13" viewBox="0 0 16 16"><rect x="1" y="2.5" width="14" height="12" rx="1" fill="none" stroke="#444" stroke-width="1.6"/><path d="M1 6.5h14M4.5 1v3M11.5 1v3" stroke="#444" stroke-width="1.6"/></svg></div>
    <div class="field" style="top:275px"><span>Residence Size</span><svg width="12" height="8" viewBox="0 0 12 8"><path d="M1 1l5 5 5-5" stroke="#444" stroke-width="1.6" fill="none"/></svg></div>
    <div class="quote-btn">SHOW MY QUOTE</div>
  </form>

  <!-- services -->
  <section class="abs services"></section>
  <div class="abs center eyebrow" style="top:697px">WHY CHOOSE US</div>
  <h2 class="abs center section-title" style="top:718px">OUR SERVICES</h2>
  <div class="abs rule" style="left:582px;top:774px"></div>
  <p class="abs services-intro">Our movers are trained to protect your belongings and your home – all pieces of furniture are padded and stretch wrapped free of charge, ensuring your items and home are damage-free at the end of your move.</p>

  <div class="abs mover-photo" role="img" aria-label="Photo of a uniformed mover pushing a hand truck stacked with boxes"></div>

  <div class="abs service" style="left:80px;top:900px">
    <svg class="diamond" viewBox="0 0 66 66"><rect x="14" y="14" width="38" height="38" transform="rotate(45 33 33)" fill="#fff" stroke="#7dc242" stroke-width="1.5"/><path d="M21 28h16v11H21zM37 31h5l3 4v4h-8z" fill="#7dc242"/><circle cx="26" cy="40" r="2.5" fill="#7dc242"/><circle cx="41" cy="40" r="2.5" fill="#7dc242"/></svg>
    <div><div class="service-name">LOCAL MOVES</div><div class="service-copy">Lorem ipsum dolor sit amet, consectetur adipiscing elit. Praesent ullamcorper massa ligula, quis aliquet diam laoreet sed.</div></div>
  </div>
  <div class="abs service" style="left:80px;top:1028px">
    <svg class="diamond" viewBox="0 0 66 66"><rect x="14" y="14" width="38" height="38" transform="rotate(45 33 33)" fill="#fff" stroke="#7dc242" stroke-width="1.5"/><path d="M33 22l12 10h-3v10H24V32h-3z" fill="#7dc242"/><rect x="30" y="35" width="6" height="7" fill="#fff"/></svg>
    <div><div class="service-name">SINGLE-FAMILY HOMES</div><div class="service-copy">Lorem ipsum dolor sit amet, consectetur adipiscing elit. Praesent ullamcorper massa ligula, quis aliquet diam laoreet sed.</div></div>
  </div>
  <div class="abs service" style="left:80px;top:1153px">
    <svg class="diamond" viewBox="0 0 66 66"><rect x="14" y="14" width="38" height="38" transform="rotate(45 33 33)" fill="#fff" stroke="#7dc242" stroke-width="1.5"/><path d="M22 25v18M44 30v13M22 34h22M22 38h22" stroke="#7dc242" stroke-width="3" fill="none"/><rect x="24" y="29" width="6" height="4" fill="#7dc242"/></svg>
    <div><div class="service-name">DORMS</div><div class="service-copy">Lorem ipsum dolor sit amet, consectetur adipiscing elit. Praesent ullamcorper massa ligula, quis aliquet diam laoreet sed.</div></div>
  </div>
  <div class="abs service" style="left:767px;top:900px">
    <svg class="diamond" viewBox="0 0 66 66"><rect x="14" y="14" width="38" height="38" transform="rotate(45 33 33)" fill="#fff" stroke="#7dc242" stroke-width="1.5"/><rect x="25" y="21" width="16" height="23" fill="#7dc242"/><path d="M28 25h3M35 25h3M28 30h3M35 30h3M28 35h3M35 35h3" stroke="#fff" stroke-width="2"/></svg>
    <div><div class="service-name">APARTMENTS</div><div class="service-copy">Lorem ipsum dolor sit amet, consectetur adipiscing elit. Praesent ullamcorper massa ligula, quis aliquet diam laoreet sed.</div></div>
  </div>
  <div class="abs service" style="left:767px;top:1028px">
    <svg class="diamond" viewBox="0 0 66 66"><rect x="14" y="14" width="38" height="38" transform="rotate(45 33 33)" fill="#fff" stroke="#7dc242" stroke-width="1.5"/><path d="M20 33l13-11 13 11" stroke="#7dc242" stroke-width="2.5" fill="none"/><path d="M24 31v12h18V31" stroke="#7dc242" stroke-width="2.5" fill="none"/><circle cx="33" cy="33" r="2.5" fill="#7dc242"/><path d="M33 36v7M30 39h6" stroke="#7dc242" stroke-width="2"/></svg>
    <div><div class="service-name">RETIREMENT COMMUNITIES</div><div class="service-copy">Lorem ipsum dolor sit amet, consectetur adipiscing elit. Praesent ullamcorper massa ligula, quis aliquet diam laoreet sed.</div></div>
  </div>
  <div class="abs service" style="left:767px;top:1153px">
    <svg class="diamond" viewBox="0 0 66 66"><rect x="14" y="14" width="38" height="38" transform="rotate(45 33 33)" fill="#fff" stroke="#7dc242" stroke-width="1.5"/><rect x="28" y="19" width="10" height="26" fill="#7dc242"/><path d="M30 23h2M34 23h2M30 28h2M34 28h2M30 33h2M34 33h2M30 38h2M34 38h2" stroke="#fff" stroke-width="1.6"/></svg>
    <div><div class="service-name">CONDOS</div><div class="service-copy">Lorem ipsum dolor sit amet, consectetur adipiscing elit. Praesent ullamcorper massa ligula, quis aliquet diam laoreet sed.</div></div>
  </div>

  <!-- testimonials -->
  <div class="abs eyebrow" style="left:80px;top:1351px">TESTIMONIALS</div>
  <h2 class="abs section-title" style="left:80px;top:1372px">WHAT CLIENTS SAY</h2>
  <div class="abs rule" style="left:80px;top:1428px"></div>
  <div class="abs card" style="left:80px;width:508px"></div>
  <div class="abs quote-mark">“</div>
  <p class="abs quote-text" style="left:116px;top:1509px;width:440px">Lorem ipsum dolor sit amet, consectetur adipiscing elit. Praesent ullamcorper massa ligula, quis aliquet diam laoreet sed. Integer faucibus mauris et nisi porta tincidunt. Pellen-tesque ultricies purus a ipsum scelerisque laoreet.</p>
  <div class="abs cite-name" style="left:114px;top:1622px">DALE RENNER</div>
  <div class="abs cite-role" style="left:114px;top:1644px">Customer</div>
  <div class="abs dots"><span></span><span></span><span></span></div>

  <!-- guarantee -->
  <div class="abs eyebrow" style="left:613px;top:1351px">BOLT HAULING</div>
  <h2 class="abs section-title" style="left:613px;top:1372px">OUR GAURANTEE</h2>
  <div class="abs rule" style="left:613px;top:1428px"></div>
  <div class="abs card" style="left:613px;width:508px"></div>
  <div class="abs" style="left:651px;top:1496px;width:440px">
    <p class="guarantee-lead">When you partner with BOLT, you'll get the best service in the industry, as well as:</p>
    <div class="perk"><svg width="13" height="11" viewBox="0 0 13 11"><path d="M1 6l4 4 7-9" stroke="#7dc242" stroke-width="2.2" fill="none"/></svg>The unlimited use of packing &amp; moving materials</div>
    <div class="perk"><svg width="13" height="11" viewBox="0 0 13 11"><path d="M1 6l4 4 7-9" stroke="#7dc242" stroke-width="2.2" fill="none"/></svg>Trained, Licensed, and Insured Movers</div>
    <div class="perk"><svg width="13" height="11" viewBox="0 0 13 11"><path d="M1 6l4 4 7-9" stroke="#7dc242" stroke-width="2.2" fill="none"/></svg>A Professional service catering to your specific needs</div>
  </div>

  <!-- newsletter -->
  <div class="abs newsletter"></div>
  <div class="abs newsletter-title">SIGN UP FOR NEWSLETTER</div>
  <div class="abs signup"><span class="signup-field">Enter Your Email</span><span class="signup-btn">JOIN</span></div>

  <!-- footer -->
  <footer class="abs footer"></footer>
  <div class="abs footer-notch"></div>
  <div class="abs footer-base"></div>

  <div class="abs f-head" style="left:80px">ABOUT US</div>
  <p class="abs f-about">At Bolt Hauling LLC, we know moving. It can be difficult, stressful, and a real pain in the backside. But it doesn't have to be! When you partner with Bolt, you get the benefits of a professional moving team that is licensed and insured for your protection along with years of experience and a dedication to providing the highest quality service, each and every time.</p>
  <div class="abs socials"><span></span><span></span><span></span><span></span><span></span></div>

  <div class="abs f-head" style="left:524px">SERVICES</div>
  <ul class="abs f-list" style="left:524px"><li>Local Moves</li><li>Apartments</li><li>Single Family Homes</li><li>Retirement Communities</li><li>Dorms</li><li>Condos</li><li>More</li></ul>

  <div class="abs f-head" style="left:716px">NEED HELP?</div>
  <ul class="abs f-list" style="left:716px"><li>Customer</li><li>Support</li><li>News</li><li>FAQ</li><li>Privacy Careers</li></ul>

  <div class="abs f-head" style="left:855px">GET IN TOUCH</div>
  <div class="abs f-contact">
    <div><svg width="11" height="14" viewBox="0 0 20 26"><path fill="#aaa" d="M10 0a9 9 0 0 0-9 9c0 7 9 17 9 17s9-10 9-17a9 9 0 0 0-9-9zm0 12.5A3.5 3.5 0 1 1 10 5.5a3.5 3.5 0 0 1 0 7z"/></svg>42 Linden Row, Maplecrest, ST 00412, US</div>
    <div><svg width="12" height="12" viewBox="0 0 24 24"><path fill="#aaa" d="M6.6 10.8a15.1 15.1 0 0 0 6.6 6.6l2.2-2.2c.3-.3.7-.4 1-.2 1.1.4 2.3.6 3.6.6.6 0 1 .4 1 1V20c0 .6-.4 1-1 1C10.6 21 3 13.4 3 4c0-.6.4-1 1-1h3.5c.6 0 1 .4 1 1 0 1.3.2 2.5.6 3.6.1.3 0 .7-.2 1z"/></svg>Phone: (555) 014-2290</div>
    <div><svg width="13" height="10" viewBox="0 0 26 18"><rect x="1" y="1" width="24" height="16" fill="none" stroke="#aaa" stroke-width="2"/><path d="M1 1l12 9 12-9" stroke="#aaa" stroke-width="2" fill="none"/></svg>E-Mail: info@bolthaulingcrew.example</div>
  </div>

  <div class="abs copyright">Copyright © 2017 &nbsp;|&nbsp; bolthaulingcrew.example. All rights reserved.</div>
  <div class="abs to-top"><svg width="14" height="9" viewBox="0 0 14 9"><path d="M1 8l6-6 6 6" stroke="#fff" stroke-width="2" fill="none"/></svg></div>

</div>
</body>
</html>
```